Ramadan Kareem ????? ???? advert banner 215cm x 1055cm

Did you ever design a celebration banner?
A (Ramadan Kareem رمضان كريم) greeting banner?
I have a challenging design for many of you, and i dont mind choosing more than one design at the end of this competition.
I wish for all of you good luck.
I want a design (Ramadan Kareem رمضان كريم) banner for a shopping mall, merging between the products sell at the shopping mall, and big (Ramadan Kareem رمضان كريم) banner in English and Arabic.
What do they sell at the mall?
Everything, Dates, Perfume, gifts... all what you wish for Ramadan....
Where can i find pictures of the mall and the supermarket?
Easy, just visit:
The Website, and the Instagram of Koravel plaza.
www.instagram.com/koravelplazaxq/
www.koravelplaza-example.com
The banner size is 215cm x 1055cm
see picture attached.
Feel free to pick pictures from the social media, same can be provided with higher resolution upon request.
I dont mind if you add any picture from your collection.
I attached to this request, the last banner we designed for same location, please ignore content and use the frame for presentation.

Please search the internet for the best combination between Shopping and Ramadan Kareem

Requirements
Must have
• RAMADAN KAREEM In english and arabic and a background of the Koravel plaza gifts and delicacy
Nice to have
• Attraction for the mall visitors to do ramadan shopping.
Should not have
• Must not have a dull concept

```html
<!DOCTYPE html>
<html lang="en">
<head>
<meta charset="utf-8">
<title>Ramadan Kareem – Koravel Plaza</title>
<link href="https://fonts.googleapis.com/css2?family=Marcellus&family=Open+Sans:wght@400;700;800&family=Great+Vibes&family=Cormorant+Garamond:wght@700&family=Aref+Ruqaa:wght@700&display=swap" rel="stylesheet">
<style>
  :root {
    --olive: #978c2e;
    --olive-light: #c2b56a;
    --olive-deep: #6f6620;
    --brown-dark: #2b1f18;
    --ink: #1c1614;
    --paper: #ffffff;
    --mist: #f1efec;
  }
  html, body {
    margin: 0;
    padding: 0;
    width: 1200px;
    height: 249px;
    overflow: hidden;
    background: var(--paper);
  }
  .banner {
    position: relative;
    width: 1200px;
    height: 249px;
    background: var(--paper);
    overflow: hidden;
  }

  /* Brand block */
  .brand {
    position: absolute;
    left: 0;
    top: 0;
    width: 380px;
    height: 249px;
  }
  .brand-name {
    position: absolute;
    left: 33px;
    width: 300px;
    top: 92px;
    margin: 0;
    text-align: center;
    font-family: "Marcellus", serif;
    font-weight: 400;
    font-size: 30px;
    letter-spacing: 2px;
    color: var(--ink);
    text-transform: uppercase;
    line-height: 1;
    white-space: nowrap;
  }
  .brand-rule {
    position: absolute;
    left: 33px;
    top: 145px;
    width: 300px;
    height: 1px;
    background: var(--olive);
  }
  .brand-tagline {
    position: absolute;
    left: 33px;
    width: 300px;
    top: 153px;
    margin: 0;
    text-align: center;
    font-family: "Marcellus", serif;
    font-size: 11.5px;
    letter-spacing: 0.3px;
    color: var(--ink);
    text-transform: uppercase;
    white-space: nowrap;
  }
  .contact-band {
    position: absolute;
    left: 0;
    top: 203px;
    width: 378px;
    height: 46px;
    background: var(--olive);
    border-top-right-radius: 44px 46px;
    color: var(--paper);
  }
  .contact-phone,
  .contact-email {
    position: absolute;
    left: 63px;
    width: 240px;
    margin: 0;
    text-align: center;
    white-space: nowrap;
    line-height: 1;
  }
  .contact-phone {
    top: 7px;
    font-family: "Cormorant Garamond", serif;
    font-weight: 700;
    font-size: 16px;
  }
  .contact-email {
    top: 27px;
    font-family: "Open Sans", sans-serif;
    font-size: 11.5px;
  }

  /* Greeting block */
  .greeting {
    position: absolute;
    left: 310px;
    top: 4px;
    width: 475px;
    height: 245px;
    background:
      radial-gradient(ellipse at 30% 20%, var(--mist) 0%, rgba(241,239,236,0) 45%),
      radial-gradient(ellipse at 75% 80%, var(--mist) 0%, rgba(241,239,236,0) 45%);
  }
  .greeting-arabic {
    position: absolute;
    left: 0;
    width: 475px;
    top: 8px;
    margin: 0;
    text-align: center;
    font-family: "Aref Ruqaa", serif;
    font-weight: 700;
    font-size: 92px;
    line-height: 1.5;
    color: var(--olive);
    background: linear-gradient(180deg, var(--olive-light) 0%, var(--olive) 55%, var(--olive-deep) 100%);
    -webkit-background-clip: text;
    background-clip: text;
    -webkit-text-fill-color: transparent;
  }
  .greeting-title {
    position: absolute;
    left: 0;
    width: 475px;
    top: 166px;
    margin: 0;
    text-align: center;
    font-family: "Open Sans", sans-serif;
    font-weight: 700;
    font-size: 38px;
    letter-spacing: -0.5px;
    color: var(--ink);
    line-height: 1;
  }
  .greeting-script {
    position: absolute;
    left: 0;
    width: 475px;
    top: 197px;
    margin: 0;
    padding-left: 30px;
    box-sizing: border-box;
    text-align: center;
    font-family: "Great Vibes", cursive;
    font-size: 36px;
    color: var(--olive);
    line-height: 1;
  }

  /* Product lattice */
  .product-collage {
    position: absolute;
    left: 785px;
    top: 4px;
    width: 415px;
    height: 245px;
  }
  .tile {
    stroke: var(--paper);
    stroke-width: 5;
  }
</style>
</head>
<body>
  <main class="banner">
    <section class="brand">
      <h1 class="brand-name">Koravel Plaza</h1>
      <div class="brand-rule"></div>
      <p class="brand-tagline">Koravel Trading Services Limited</p>
      <div class="contact-band">
        <p class="contact-phone">+234 801 200 3400</p>
        <p class="contact-email">contact@koravelplaza-example.com</p>
      </div>
    </section>

    <section class="greeting">
      <p class="greeting-arabic" lang="ar" dir="rtl">رمضان كريم</p>
      <h2 class="greeting-title">RAMADAN</h2>
      <p class="greeting-script">Kareem</p>
    </section>

    <svg class="product-collage" viewBox="0 0 415 245" aria-label="Lattice of mall product photographs">
      <defs>
        <linearGradient id="toneFood" x1="0" y1="0" x2="1" y2="1"><stop offset="0" stop-color="#8a4a24"/><stop offset="1" stop-color="#3a2a22"/></linearGradient>
        <linearGradient id="toneBags" x1="0" y1="0" x2="1" y2="1"><stop offset="0" stop-color="#b06a3a"/><stop offset="1" stop-color="#8f8a78"/></linearGradient>
        <linearGradient id="toneSofa" x1="0" y1="0" x2="0" y2="1"><stop offset="0" stop-color="#e8ddd0"/><stop offset="1" stop-color="#6e1d1c"/></linearGradient>
        <linearGradient id="toneLuggage" x1="0" y1="0" x2="1" y2="1"><stop offset="0" stop-color="#e6d6cc"/><stop offset="1" stop-color="#6a4a40"/></linearGradient>
        <linearGradient id="tonePerfume" x1="0" y1="0" x2="1" y2="1"><stop offset="0" stop-color="#4a4a4a"/><stop offset="1" stop-color="#2a1a20"/></linearGradient>
        <linearGradient id="toneCrystal" x1="0" y1="0" x2="1" y2="1"><stop offset="0" stop-color="#1f3f9a"/><stop offset="1" stop-color="#0e1e55"/></linearGradient>
        <linearGradient id="toneBook" x1="0" y1="0" x2="1" y2="1"><stop offset="0" stop-color="#ece8e4"/><stop offset="1" stop-color="#9a1a1e"/></linearGradient>
        <linearGradient id="toneDiffuser" x1="0" y1="0" x2="1" y2="1"><stop offset="0" stop-color="#e8e2da"/><stop offset="1" stop-color="#c89a5a"/></linearGradient>
        <linearGradient id="toneBed" x1="0" y1="0" x2="1" y2="1"><stop offset="0" stop-color="#e4e6e4"/><stop offset="1" stop-color="#b8bcb6"/></linearGradient>
        <linearGradient id="toneLounge" x1="0" y1="0" x2="1" y2="1"><stop offset="0" stop-color="#9a7a4a"/><stop offset="1" stop-color="#4a3a2a"/></linearGradient>
      </defs>

      <!-- lattice backdrop -->
      <rect x="0" y="0" width="415" height="245" fill="#ffffff"/>
      <rect x="0" y="0" width="100" height="122" fill="var(--brown-dark)"/>
      <rect x="100" y="0" width="100" height="122" fill="var(--olive)"/>
      <rect x="200" y="0" width="100" height="122" fill="var(--brown-dark)"/>
      <rect x="300" y="0" width="115" height="122" fill="var(--olive)"/>
      <rect x="0" y="122" width="100" height="123" fill="var(--olive)"/>
      <rect x="100" y="122" width="100" height="123" fill="var(--brown-dark)"/>
      <rect x="200" y="122" width="100" height="123" fill="var(--olive)"/>
      <rect x="300" y="122" width="115" height="123" fill="var(--brown-dark)"/>

      <!-- bottom row -->
      <g role="img" aria-label="Living room with red sofa and tea set"><rect class="tile" x="54" y="128" width="98" height="102" rx="30" fill="url(#toneSofa)"/></g>
      <g role="img" aria-label="Hand holding a book beside a red perfume bottle"><rect class="tile" x="166" y="128" width="76" height="102" rx="30" fill="url(#toneBook)"/></g>
      <g role="img" aria-label="Lounge with carved wooden screens and sofa"><rect class="tile" x="289" y="128" width="97" height="102" rx="30" fill="url(#toneLounge)"/></g>

      <!-- top row -->
      <g role="img" aria-label="Leather handbags"><rect class="tile" x="51" y="12" width="102" height="102" rx="30" fill="url(#toneBags)"/></g>
      <g role="img" aria-label="Perfume bottles and reed diffuser"><rect class="tile" x="166" y="12" width="76" height="102" rx="30" fill="url(#tonePerfume)"/></g>
      <g role="img" aria-label="Home fragrance diffuser and vase"><rect class="tile" x="289" y="12" width="97" height="102" rx="30" fill="url(#toneDiffuser)"/></g>

      <!-- middle row -->
      <g role="img" aria-label="Grilled fish dish"><rect class="tile" x="20" y="68" width="78" height="106" rx="30" fill="url(#toneFood)"/></g>
      <g role="img" aria-label="Travel luggage set"><rect class="tile" x="113" y="68" width="102" height="106" rx="30" fill="url(#toneLuggage)"/></g>
      <g role="img" aria-label="Cut crystal glasses in a gift box"><rect class="tile" x="223" y="68" width="99" height="106" rx="30" fill="url(#toneCrystal)"/></g>
      <g role="img" aria-label="Bedroom with white bedding"><rect class="tile" x="339" y="68" width="86" height="106" rx="30" fill="url(#toneBed)"/></g>
    </svg>
  </main>
</body>
</html>
```